Brackwell Removals

We are a domestic removals company, providing the following service:
- removals service
- packing service
- packing materials
- storage facility
- furniture dismantling and reassembling
We would like to start a flyer campaign to customers that just agreed for the house sale.
Our strong key points:
- Good Reviews (Ratewise, Zenquor, trulyshifting.com and plazabook)
- Two Men Service (we do all the heavy work for the customer, and place the furniture and boxes to each room of destination)
- Fully Insured
- We can take bookings 7-days of week
- Free and no-obligation survey (we need to do a house visit first in order to provide a fixed and accurate quote)
- Free Quote
Technical Specs:
Landline number: 01632 960418
Contact email: office@brackwellremovals.example.co.uk
Address: Unit 14, Corrin Lane, Northampton NN9 4XQ
Website: brackwellremovals.example.co.uk
Took a look on the onto previous projects on PV.com, and liked several flyers already done by you guys, for this industry
We'd like to integrate the colours from our logo in the flyer as well !!

```html
<!DOCTYPE html>
<html lang="en">
<head>
<meta charset="utf-8">
<title>Brackwell Removals – Flyer</title>
<link rel="stylesheet" href="https://fonts.googleapis.com/css2?family=Saira+Condensed:wght@700;800&family=Lato:wght@400;700&display=swap">
<style>
  :root {
    --teal: #17788a;
    --orange: #f0592a;
    --white: #ffffff;
    --page: #e8e9eb;
    --ink: #ffffff;
  }
  * { box-sizing: border-box; margin: 0; padding: 0; }
  html, body { width: 1200px; height: 984px; overflow: hidden; }
  body { background: var(--page); font-family: "Lato", sans-serif; position: relative; }

  .flyer {
    position: absolute; left: 270px; top: 25px;
    width: 660px; height: 934px;
    background: var(--white); overflow: hidden;
    box-shadow: 0 4px 14px rgba(0,0,0,.25);
  }
  .flyer-shapes { position: absolute; inset: 0; }

  .brand {
    position: absolute; left: 40px; top: 70px; width: 220px;
    display: flex; align-items: center; gap: 10px;
  }
  .brand-dot { width: 26px; height: 26px; border-radius: 50%; background: var(--orange); flex: none; }
  .brand-name {
    font-family: "Saira Condensed", sans-serif; font-weight: 800;
    color: var(--white); font-size: 34px; line-height: 0.95; letter-spacing: .5px;
  }

  .headline {
    position: absolute; left: 240px; top: 38px; width: 390px;
    text-align: center; color: var(--white);
    font-family: "Saira Condensed", sans-serif; font-weight: 800;
    font-size: 50px; line-height: 52px; letter-spacing: 1px;
  }

  .services {
    position: absolute; top: 272px; left: 44px; right: 30px;
    display: grid; grid-template-columns: 270px 1fr;
    font-family: "Saira Condensed", sans-serif; font-weight: 700;
    color: var(--orange); font-size: 27px; line-height: 30px; letter-spacing: .4px;
  }
  .services ul { list-style: none; }
  .services li { display: flex; align-items: center; gap: 8px; }
  .services li.cont { padding-left: 28px; }
  .tick { width: 20px; height: 20px; flex: none; }

  .photo { position: absolute; }
  .photo-circle { border-radius: 50%; border: 5px solid var(--teal); }
  .photo-pack { left: 221px; top: 378px; width: 124px; height: 124px;
    background: radial-gradient(circle at 40% 40%, #c9a27a, #2d3f6b); }
  .photo-boxes { left: 358px; top: 372px; width: 146px; height: 146px;
    background: radial-gradient(circle at 45% 45%, #d8b78c, #6e5a45); }
  .photo-store { left: 520px; top: 413px; width: 116px; height: 116px;
    background: linear-gradient(180deg, #e0e4ea, #4a6fb1 60%, #d98a3a); }
  .photo-movers { left: 250px; top: 500px; width: 410px; height: 358px;
    background: linear-gradient(160deg, #f3f3f3 0%, #d9b88f 45%, #1f2e5a 80%);
    -webkit-mask-image: linear-gradient(90deg, transparent 0%, #000 22%);
    mask-image: linear-gradient(90deg, transparent 0%, #000 22%); }

  .keypoints { position: absolute; left: 37px; top: 489px; width: 222px; color: var(--ink); }
  .keypoints h2 {
    font-family: "Saira Condensed", sans-serif; font-weight: 800;
    font-size: 38px; line-height: 36px; margin-bottom: 6px; letter-spacing: .5px;
  }
  .keypoints ul { list-style: none; }
  .keypoints li { display: flex; gap: 7px; margin-bottom: 9px; }
  .keypoints .tick { width: 14px; height: 14px; margin-top: 2px; }
  .kp-title { font-weight: 700; font-size: 14px; line-height: 16px; text-transform: uppercase; }
  .kp-note { font-size: 10.5px; line-height: 13px; }

  .contact {
    position: absolute; left: 0; right: 0; top: 860px; height: 74px;
    background: var(--teal); color: var(--white);
    text-align: center; font-size: 13px; line-height: 16px; padding-top: 8px;
  }
  .contact strong { font-weight: 700; }
</style>
</head>
<body>
<main class="flyer">
  <svg class="flyer-shapes" width="660" height="934" viewBox="0 0 660 934" aria-hidden="true">
    <path d="M0 218 Q330 250 660 212 V232 Q330 272 0 240 Z" fill="var(--orange)"/>
    <path d="M0 0 H660 V210 Q330 248 0 212 Z" fill="var(--teal)"/>
    <path d="M0 454 Q300 430 660 418 V860 H0 Z" fill="var(--teal)"/>
    <path d="M0 468 Q300 444 660 434 V860 H0 Z" fill="var(--orange)"/>
  </svg>

  <div class="brand">
    <span class="brand-dot"></span>
    <span class="brand-name">BRACKWELL<br>REMOVALS</span>
  </div>

  <h1 class="headline">REMOVALS IN<br>NORTHAMPTON &amp;<br>SURROUNDINGS</h1>

  <section class="services">
    <ul>
      <li><svg class="tick" viewBox="0 0 20 20"><circle cx="9" cy="11" r="7.5" fill="none" stroke="var(--teal)" stroke-width="2"/><path d="M5 11l3.5 3L18 3" fill="none" stroke="var(--teal)" stroke-width="2.4"/></svg>REMOVALS SERVICE</li>
      <li><svg class="tick" viewBox="0 0 20 20"><circle cx="9" cy="11" r="7.5" fill="none" stroke="var(--teal)" stroke-width="2"/><path d="M5 11l3.5 3L18 3" fill="none" stroke="var(--teal)" stroke-width="2.4"/></svg>PACKING SERVICE</li>
      <li><svg class="tick" viewBox="0 0 20 20"><circle cx="9" cy="11" r="7.5" fill="none" stroke="var(--teal)" stroke-width="2"/><path d="M5 11l3.5 3L18 3" fill="none" stroke="var(--teal)" stroke-width="2.4"/></svg>PACKING MATERIALS</li>
    </ul>
    <ul>
      <li><svg class="tick" viewBox="0 0 20 20"><circle cx="9" cy="11" r="7.5" fill="none" stroke="var(--teal)" stroke-width="2"/><path d="M5 11l3.5 3L18 3" fill="none" stroke="var(--teal)" stroke-width="2.4"/></svg>STORAGE FACILITY</li>
      <li><svg class="tick" viewBox="0 0 20 20"><circle cx="9" cy="11" r="7.5" fill="none" stroke="var(--teal)" stroke-width="2"/><path d="M5 11l3.5 3L18 3" fill="none" stroke="var(--teal)" stroke-width="2.4"/></svg>FURNITURE DISMANTLING</li>
      <li class="cont">AND REASSEMBLING</li>
    </ul>
  </section>

  <div class="photo photo-movers" role="img" aria-label="Two removal workers in overalls carrying cardboard boxes beside a white van"></div>
  <div class="photo photo-circle photo-pack" role="img" aria-label="Hands sealing a cardboard box with packing tape"></div>
  <div class="photo photo-circle photo-boxes" role="img" aria-label="Worker checking stacked cardboard boxes"></div>
  <div class="photo photo-circle photo-store" role="img" aria-label="Storage warehouse with tall shelving racks"></div>

  <section class="keypoints">
    <h2>OUR STRONG<br>KEY POINTS:</h2>
    <ul>
      <li><svg class="tick" viewBox="0 0 20 20"><circle cx="9" cy="11" r="7.5" fill="none" stroke="#fff" stroke-width="2"/><path d="M5 11l3.5 3L18 3" fill="none" stroke="#fff" stroke-width="2.4"/></svg>
        <div><p class="kp-title">Good Reviews</p><p class="kp-note">(Ratewise, Zenquor, trulyshifting.com and plazabook)</p></div></li>
      <li><svg class="tick" viewBox="0 0 20 20"><circle cx="9" cy="11" r="7.5" fill="none" stroke="#fff" stroke-width="2"/><path d="M5 11l3.5 3L18 3" fill="none" stroke="#fff" stroke-width="2.4"/></svg>
        <div><p class="kp-title">Two Men Service</p><p class="kp-note">(we do all the heavy work for the customer, and place the furniture and boxes to each room of destination)</p></div></li>
      <li><svg class="tick" viewBox="0 0 20 20"><circle cx="9" cy="11" r="7.5" fill="none" stroke="#fff" stroke-width="2"/><path d="M5 11l3.5 3L18 3" fill="none" stroke="#fff" stroke-width="2.4"/></svg>
        <div><p class="kp-title">Fully Insured</p></div></li>
      <li><svg class="tick" viewBox="0 0 20 20"><circle cx="9" cy="11" r="7.5" fill="none" stroke="#fff" stroke-width="2"/><path d="M5 11l3.5 3L18 3" fill="none" stroke="#fff" stroke-width="2.4"/></svg>
        <div><p class="kp-title">We can take bookings<br>7-days of week</p></div></li>
      <li><svg class="tick" viewBox="0 0 20 20"><circle cx="9" cy="11" r="7.5" fill="none" stroke="#fff" stroke-width="2"/><path d="M5 11l3.5 3L18 3" fill="none" stroke="#fff" stroke-width="2.4"/></svg>
        <div><p class="kp-title">Free and no-obligation survey</p><p class="kp-note">(we need to do a house visit first in order to provide a fixed and accurate quote)</p></div></li>
      <li><svg class="tick" viewBox="0 0 20 20"><circle cx="9" cy="11" r="7.5" fill="none" stroke="#fff" stroke-width="2"/><path d="M5 11l3.5 3L18 3" fill="none" stroke="#fff" stroke-width="2.4"/></svg>
        <div><p class="kp-title">Free Quote</p></div></li>
    </ul>
  </section>

  <footer class="contact">
    <p>CONTACT INFO:</p>
    <p><strong>Ph: 01632 960418 | Email: office@brackwellremovals.example.co.uk | Web: brackwellremovals.example.co.uk</strong></p>
    <p><strong>Add: Unit 14, Corrin Lane, Northampton NN9 4XQ</strong></p>
  </footer>
</main>
</body>
</html>
```